Banner Design für  Software für Finanzintermediäre
Banner Design für Software für Finanzintermediäre
Zielgruppe
Software/Applikation für Finanzintermediäre (Vermögensverwalter, Family Office, Privat Banker)
Aufgabenstellung
Für verschiedene Kommunikationsmassnahmen (Social Media, Fact Sheets oder Webseiten) benötigen wir Bildlogo/Banner für Zusammenarbeit mit Partner.
Botschaft: Partnerunternehmen (mit Logo) Inside OLVARQUENTIX. Das Bildlogo sollte flexibel angepasst werden können (neuer Partner). Auf dieser Basis sollten auch Bildbanner für den Transport von Botschaften aufgebaut werden können. Folgeaufträge sind möglich. Rohdaten werden erwünscht.
Logos OLVARQUENTIX sowie Partnerlogos liegen bei. Beispiele als Idee für eine Umsetzung von Velmora Outlook liegen bei. Es wird aber eine eigene Kreation erwünscht

```html
<!DOCTYPE html>
<html lang="en">
<head>
<meta charset="utf-8">
<title>OLVARQUENTIX Banners</title>
<link rel="stylesheet" href="https://fonts.googleapis.com/css2?family=Roboto+Condensed:wght@300;500;700&display=swap">
<style>
  :root {
    --page-bg: #ffffff;
    --text-light: #ffffff;
    --slate-top: #6a8193;
    --slate-mid: #56707f;
    --slate-low: #4a6172;
    --suit-dark: #1c2530;
    --board-blue: #4d6f9c;
    --hand-warm: #b59584;
    --navy-deep: #14314f;
    --navy-mid: #234566;
    --navy-core: #101f33;
    --paper-light: #c3ccd5;
    --paper-mid: #8ea2b6;
    --rock-dark: #33373d;
    --sky-top: #76818f;
    --sky-mid: #8791a0;
    --mist-light: #a3adb9;
    --ridge-mid: #5f6977;
  }
  * { margin: 0; padding: 0; box-sizing: border-box; }
  html, body {
    width: 1059px;
    height: 1200px;
    overflow: hidden;
    background: var(--page-bg);
  }
  body {
    position: relative;
    font-family: "Roboto Condensed", "Arial Narrow", sans-serif;
    color: var(--text-light);
  }
  .banner {
    position: absolute;
    width: 737px;
    height: 280px;
    overflow: hidden;
  }
  .banner--target  { left: 125px; top: 58px; }
  .banner--compass { left: 127px; top: 432px; }
  .banner--summit  { left: 130px; top: 821px; }

  .banner__photo {
    position: absolute;
    inset: 0;
  }
  .banner--target .banner__photo {
    background:
      radial-gradient(ellipse 110px 40px at 500px 255px, rgba(181,149,132,0.85) 0%, rgba(181,149,132,0) 100%),
      radial-gradient(ellipse 95px 85px at 525px 155px, rgba(200,212,228,0.55) 0%, rgba(77,111,156,0.75) 45%, rgba(77,111,156,0) 100%),
      radial-gradient(ellipse 70px 45px at 450px 70px, rgba(77,111,156,0.6) 0%, rgba(77,111,156,0) 100%),
      radial-gradient(ellipse 150px 220px at 700px 170px, rgba(28,37,48,0.95) 0%, rgba(28,37,48,0.85) 55%, rgba(28,37,48,0) 100%),
      linear-gradient(180deg, var(--slate-top) 0%, var(--slate-mid) 55%, var(--slate-low) 100%);
  }
  .banner--compass .banner__photo {
    background:
      radial-gradient(circle 150px at 385px 175px, var(--navy-core) 0%, #1b3150 60%, rgba(40,70,100,0.9) 80%, rgba(40,70,100,0) 100%),
      radial-gradient(ellipse 100px 60px at 360px 30px, rgba(140,160,180,0.5) 0%, rgba(140,160,180,0) 100%),
      radial-gradient(ellipse 120px 200px at 650px 130px, rgba(195,204,213,0.9) 0%, rgba(142,162,182,0.7) 55%, rgba(142,162,182,0) 100%),
      linear-gradient(90deg, var(--navy-deep) 0%, var(--navy-mid) 35%, var(--paper-mid) 75%, #3d5f82 100%);
  }
  .banner--summit .banner__photo {
    background:
      radial-gradient(ellipse 150px 180px at 110px 260px, var(--rock-dark) 0%, var(--rock-dark) 65%, rgba(51,55,61,0) 100%),
      radial-gradient(ellipse 260px 40px at 430px 205px, rgba(163,173,185,0.7) 0%, rgba(163,173,185,0) 100%),
      radial-gradient(ellipse 330px 70px at 520px 260px, rgba(95,105,119,0.95) 0%, rgba(95,105,119,0) 100%),
      radial-gradient(ellipse 180px 60px at 560px 185px, rgba(95,105,119,0.8) 0%, rgba(95,105,119,0) 100%),
      linear-gradient(180deg, var(--sky-top) 0%, var(--sky-mid) 55%, #6c7685 100%);
  }

  .brand {
    position: absolute;
    top: 14px;
    right: 18px;
    display: flex;
    align-items: center;
    gap: 14px;
  }
  .brand__name {
    font-weight: 500;
    font-size: 29px;
    letter-spacing: 0.5px;
    line-height: 1;
  }
  .brand__mark {
    width: 28px;
    height: 24px;
    background: var(--text-light);
  }

  .headline {
    position: absolute;
    font-size: 41px;
    line-height: 47px;
    letter-spacing: -0.3px;
  }
  .headline__light { font-weight: 300; display: block; }
  .headline__bold  { font-weight: 700; display: block; }

  .banner--target .headline,
  .banner--compass .headline {
    left: 38px;
    top: 118px;
  }
  .banner--summit .headline {
    left: 0;
    width: 782px;
    top: 98px;
    text-align: center;
  }
</style>
</head>
<body>

  <section class="banner banner--target">
    <div class="banner__photo" role="img" aria-label="Hand in a dark suit holding a floating dartboard with three darts in the bullseye"></div>
    <div class="brand">
      <span class="brand__name">OLVARQUENTIX</span>
      <span class="brand__mark"></span>
    </div>
    <h2 class="headline">
      <span class="headline__light">Prepare for the</span>
      <span class="headline__bold">target market</span>
      <span class="headline__light">requirements</span>
    </h2>
  </section>

  <section class="banner banner--compass">
    <div class="banner__photo" role="img" aria-label="Compass lying on printed financial tables with columns of figures"></div>
    <div class="brand">
      <span class="brand__name">OLVARQUENTIX</span>
      <span class="brand__mark"></span>
    </div>
    <h2 class="headline">
      <span class="headline__light">Prepare for the</span>
      <span class="headline__bold">target market</span>
      <span class="headline__light">requirements</span>
    </h2>
  </section>

  <section class="banner banner--summit">
    <div class="banner__photo" role="img" aria-label="Person with raised arms standing on a cliff edge above a misty mountain range"></div>
    <div class="brand">
      <span class="brand__name">OLVARQUENTIX</span>
      <span class="brand__mark"></span>
    </div>
    <h2 class="headline">
      <span class="headline__bold">Our universe</span>
      <span class="headline__light">is expanding</span>
    </h2>
  </section>

</body>
</html>
```